Darrow Consulting needs a quality & professional business card!

I am a recruitment and employment consultant from Brisbane, Australia and I had a fantastic logo organised by this community to I am hoping the business card will be the same.

I have attached the Darrow consulting logo that ideally would feature on the back of the business card. There are a number of logos for you to use as you see fit. I would like the colour cheme to match that of the Darrow Consulting logo. I also have a secondary company called Career Lantern Australia and I have included that logo as well. While it is an important part of the business I don't want this logo feature too predominantly as I am moving out of this space. This logo was created by myself and is of low quality. Feel free to use the icon and words however you want. The winning design will be smart, professional and eye-catching.

The information I am looking for in the business card is:
Name: Gavin Darrow
Position: Founder & Director
Phone: (07) 3519 6482
Mobile: 0431 586 207
Email: gavin@careerlantern.com.au

Target Market(s)

Recruiters, government, large companies

Contact Information for Business Card

Name: Gavin Darrow
Phone: (07) 3519 6482
Mobile: 0431 586 207
Web: www.careerlantern.com.au

Font styles to use
Serif
Sans Serif

Requirements
Must have
• Darrow Consulting Logo on reverse side
• Contact details on front side with smaller reference to Darrow Consulting logo and Career Lantern Australia logo

```html
<!DOCTYPE html>
<html lang="en">
<head>
<meta charset="utf-8">
<title>Darrow Consulting — Business Card</title>
<link rel="stylesheet" href="https://fonts.googleapis.com/css2?family=Barlow+Condensed:wght@400&family=Barlow+Semi+Condensed:wght@500&family=Montserrat:wght@400&display=swap">
<style>
  :root {
    --backdrop: #2474b4;
    --card-white: #ffffff;
    --card-dark: #24272a;
    --brand-blue: #0091c9;
    --brand-orange: #df8133;
    --brand-green: #00a651;
    --ink: #222222;
    --ink-soft: #2b2b2b;
    --logo-light: #c9c9c9;
  }
  * { margin: 0; padding: 0; box-sizing: border-box; }
  html, body { width: 1200px; height: 1200px; overflow: hidden; }
  body { background: var(--backdrop); position: relative; font-family: "Barlow Condensed", sans-serif; }

  .card { position: absolute; width: 646px; height: 387px; overflow: hidden; }
  .card-front { left: 274px; top: 153px; background: var(--card-white); border-radius: 22px; }
  .card-back { left: 285px; top: 667px; background: var(--card-dark); border-radius: 28px; }

  .color-band { position: absolute; left: 0; width: 100%; height: 35px; display: flex; }
  .color-band.top { top: 0; }
  .color-band.bottom { bottom: 0; }
  .color-band span { flex: 1; }
  .band-blue { background: var(--brand-blue); }
  .band-orange { background: var(--brand-orange); }
  .band-green { background: var(--brand-green); }

  .holder-name {
    position: absolute; left: 44px; top: 58px;
    font-family: "Barlow Semi Condensed", sans-serif; font-weight: 500;
    font-size: 31px; line-height: 1; color: var(--brand-blue);
  }
  .holder-role {
    position: absolute; left: 44px; top: 95px;
    font-size: 20px; line-height: 1; color: var(--ink-soft);
  }

  .contact-list { position: absolute; right: 42px; top: 230px; list-style: none; text-align: right; }
  .contact-list li {
    display: flex; justify-content: flex-end; align-items: center; gap: 8px;
    height: 29.5px; font-size: 22px; color: var(--ink-soft);
  }
  .contact-list svg { width: 18px; height: 18px; fill: var(--brand-blue); flex: none; }

  .partner-names { position: absolute; left: 38px; top: 306px; display: flex; align-items: center; gap: 20px; }
  .partner-name {
    display: flex; align-items: center; gap: 6px;
    font-family: "Montserrat", sans-serif; font-weight: 400;
    font-size: 12px; color: var(--ink);
  }
  .partner-name .mark { width: 12px; height: 12px; background: var(--ink); border-radius: 50%; }

  .back-brand {
    position: absolute; left: 0; top: 0; width: 100%; height: 100%;
    display: flex; justify-content: center; align-items: center; gap: 12px;
    font-family: "Montserrat", sans-serif; font-weight: 400;
    font-size: 28px; color: var(--logo-light); letter-spacing: 1px;
  }
  .back-brand .mark { width: 22px; height: 22px; background: var(--logo-light); }
</style>
</head>
<body>

<section class="card card-front" aria-label="Business card front">
  <div class="color-band top">
    <span class="band-blue"></span><span class="band-orange"></span><span class="band-green"></span><span class="band-blue"></span>
  </div>

  <h1 class="holder-name">Gavin Darrow</h1>
  <p class="holder-role">Founder &amp; Director</p>

  <div class="partner-names">
    <span class="partner-name"><i class="mark"></i>Career Lantern Australia</span>
    <span class="partner-name">Darrow Consulting</span>
  </div>

  <ul class="contact-list">
    <li>(07) 3519 6482
      <svg viewBox="0 0 24 24" aria-hidden="true"><path d="M20 15.5c-1.2 0-2.4-.2-3.6-.6a1 1 0 0 0-1 .25l-2.2 2.2a15 15 0 0 1-6.6-6.6l2.2-2.2a1 1 0 0 0 .25-1A11.4 11.4 0 0 1 8.5 4a1 1 0 0 0-1-1H4a1 1 0 0 0-1 1 17 17 0 0 0 17 17 1 1 0 0 0 1-1v-3.5a1 1 0 0 0-1-1z"/></svg>
    </li>
    <li>0431 586 207
      <svg viewBox="0 0 24 24" aria-hidden="true"><path d="M2 9c2-3 6-4 10-4s8 1 10 4l-1.5 2.5-3.5-1V8c-1.6-.5-3.3-.7-5-.7S8.6 7.5 7 8v2.5l-3.5 1z"/><path d="M6 12h12l2 8H4zm6 2a2.5 2.5 0 1 0 0 5 2.5 2.5 0 0 0 0-5z"/></svg>
    </li>
    <li>gavin@careerlantern.com.au
      <svg viewBox="0 0 24 24" aria-hidden="true"><path d="M2 5h20v2l-10 6L2 7z"/><path d="M2 9l10 6 10-6v10H2z"/></svg>
    </li>
    <li>www.careerlantern.com.au
      <svg viewBox="0 0 24 24" aria-hidden="true"><path d="M12 2a10 10 0 1 0 0 20 10 10 0 0 0 0-20zm6.9 6h-3a15 15 0 0 0-1.3-3.9A8 8 0 0 1 18.9 8zM12 4c.8 1.1 1.5 2.5 1.9 4h-3.8c.4-1.5 1.1-2.9 1.9-4zM4.3 14a8 8 0 0 1 0-4h3.4a16 16 0 0 0 0 4zm.8 2h3a15 15 0 0 0 1.3 3.9A8 8 0 0 1 5.1 16zm3-8h-3a8 8 0 0 1 4.3-3.9C8.8 5.3 8.4 6.6 8.1 8zM12 20c-.8-1.1-1.5-2.5-1.9-4h3.8c-.4 1.5-1.1 2.9-1.9 4zm2.3-6H9.7a14 14 0 0 1 0-4h4.6a14 14 0 0 1 0 4zm.3 5.9c.6-1.2 1-2.5 1.3-3.9h3a8 8 0 0 1-4.3 3.9zm1.7-5.9a16 16 0 0 0 0-4h3.4a8 8 0 0 1 0 4z"/></svg>
    </li>
  </ul>

  <div class="color-band bottom">
    <span class="band-blue"></span><span class="band-green"></span><span class="band-orange"></span><span class="band-blue"></span>
  </div>
</section>

<section class="card card-back" aria-label="Business card back">
  <div class="back-brand"><i class="mark"></i>Darrow Consulting</div>
</section>

</body>
</html>
```